Stationery Design Project

Need stationery designed for our chicken farming business. We grow chickens in barns for meat production. Looking for all stationery items (business cards, letterhead, envelopes, with compliments etc).
Updates

Reason: I am going away for 5 days from Friday 30/3/2012. Won't be able to check designs.

Target Market(s)

The stationery will only be used for correspondence with key stakeholders / suppliers. It is not to be used for marketing etc.

Industry/Entity Type

Business

Requirements
Must have
• I have included all the contact details required for each type of stationery.
Nice to have
• Colours to be used white, green, red, yellow and black (see design).
Should not have
• Rounded Corners.
Centralised information (in centre of business cards / letterhead etc).

```html
<!DOCTYPE html>
<html lang="en">
<head>
<meta charset="utf-8">
<title>Brookvale Poultry Stationery</title>
<link rel="stylesheet" href="https://fonts.googleapis.com/css2?family=Source+Sans+3:wght@400;600&display=swap">
<style>
  :root {
    --backdrop: #e9e6e1;
    --paper: #ffffff;
    --green: #1f6b4a;
    --red: #a3202a;
    --yellow: #f5a623;
    --ink: #222222;
    --muted: #555555;
    --rule: #333333;
  }
  * { box-sizing: border-box; margin: 0; padding: 0; }
  html, body { width: 1200px; height: 851px; overflow: hidden; }
  body {
    background: var(--backdrop);
    font-family: "Source Sans 3", Arial, sans-serif;
    color: var(--ink);
    position: relative;
  }
  .sheet {
    position: absolute;
    top: 46px;
    width: 565px;
    height: 731px;
    background: var(--paper);
    box-shadow: 0 2px 8px rgba(0,0,0,0.25);
    overflow: hidden;
  }
  .sheet--letterhead { left: 17px; }
  .sheet--fax { left: 607px; }

  .brand {
    position: absolute;
    left: 49px;
    top: 28px;
    display: flex;
    align-items: center;
    gap: 7px;
    color: var(--green);
    font-weight: 600;
    font-size: 18px;
    line-height: 1;
  }
  .brand__dot {
    width: 26px; height: 26px;
    border-radius: 50%;
    background: var(--red);
  }

  .contact {
    position: absolute;
    left: 417px;
    top: 22px;
    border-left: 1px solid #999;
    padding-left: 8px;
    font-size: 8.5px;
    line-height: 11px;
    color: var(--muted);
  }
  .sheet--fax .contact { left: 416px; top: 14px; }
  .contact__row { display: flex; align-items: center; gap: 5px; }
  .contact__icon { width: 7px; height: 7px; flex: none; }
  .contact__gap { height: 3px; }

  .footer {
    position: absolute;
    left: 0; bottom: 0;
    width: 100%;
  }
  .footer__stripe { height: 3px; }
  .footer__stripe--red { background: var(--red); }
  .footer__stripe--yellow { background: var(--yellow); margin-top: 3px; }
  .footer__band {
    margin-top: 3px;
    height: 58px;
    background: var(--green);
    color: #ffffff;
    font-size: 8.5px;
    line-height: 10px;
    text-align: right;
    padding: 10px 50px 0 0;
  }
  .sheet--fax .footer__band { padding-top: 28px; }
  .footer__street { margin-top: 7px; }
  .sheet--fax .footer__street { margin-top: 0; }

  .fax-title {
    position: absolute;
    left: 48px;
    top: 183px;
    font-size: 36px;
    font-weight: 400;
    letter-spacing: 0.5px;
  }
  .fax-fields {
    position: absolute;
    left: 48px;
    top: 234px;
    width: 482px;
  }
  .fax-fields__row {
    display: flex;
    gap: 12px;
    height: 30px;
    align-items: flex-end;
  }
  .fax-field {
    border-bottom: 1px solid var(--rule);
    font-size: 9.5px;
    padding-bottom: 2px;
  }
  .fax-field--wide { width: 276px; }
  .fax-field--narrow { flex: 1; }

  .fax-options {
    position: absolute;
    top: 388px;
    left: 48px;
    width: 482px;
    font-size: 9.5px;
  }
  .fax-option {
    position: absolute;
    display: flex;
    align-items: center;
    gap: 6px;
    white-space: nowrap;
  }
  .fax-option__box {
    width: 12px; height: 12px;
    border: 1px solid var(--rule);
  }
</style>
</head>
<body>

  <section class="sheet sheet--letterhead">
    <div class="brand"><span class="brand__dot"></span>Brookvale Poultry Pty Ltd</div>
    <div class="contact">
      <div class="contact__row"><svg class="contact__icon" viewBox="0 0 10 10"><path d="M2 1h2l1 2-1 1a5 5 0 0 0 2 2l1-1 2 1v2c-4 1-8-3-7-7z" fill="var(--yellow)"/></svg>041 555 0142</div>
      <div class="contact__row"><svg class="contact__icon" viewBox="0 0 10 10"><rect x="1" y="3" width="8" height="5" fill="var(--yellow)"/><rect x="3" y="1" width="4" height="2" fill="var(--yellow)"/></svg>088 555 0176</div>
      <div class="contact__row"><svg class="contact__icon" viewBox="0 0 10 10"><circle cx="5" cy="5" r="4" fill="none" stroke="var(--yellow)" stroke-width="1.5"/></svg>office@brookvalepoultry.com</div>
    </div>

    <footer class="footer">
      <div class="footer__stripe footer__stripe--red"></div>
      <div class="footer__stripe footer__stripe--yellow"></div>
      <div class="footer__band">
        <div>PO Box 427</div>
        <div>MARLOW BEND SA 5261</div>
        <div class="footer__street">Settlers Corner Road KERRIDGE SA 5258</div>
      </div>
    </footer>
  </section>

  <section class="sheet sheet--fax">
    <div class="brand"><span class="brand__dot"></span>Brookvale Poultry Pty Ltd</div>
    <div class="contact">
      <div>PO Box 427</div>
      <div>MARLOW BEND SA 5261</div>
      <div class="contact__gap"></div>
      <div class="contact__row"><svg class="contact__icon" viewBox="0 0 10 10"><path d="M2 1h2l1 2-1 1a5 5 0 0 0 2 2l1-1 2 1v2c-4 1-8-3-7-7z" fill="var(--yellow)"/></svg>041 555 0142</div>
      <div class="contact__row"><svg class="contact__icon" viewBox="0 0 10 10"><rect x="1" y="3" width="8" height="5" fill="var(--yellow)"/><rect x="3" y="1" width="4" height="2" fill="var(--yellow)"/></svg>088 555 0176</div>
      <div class="contact__row"><svg class="contact__icon" viewBox="0 0 10 10"><circle cx="5" cy="5" r="4" fill="none" stroke="var(--yellow)" stroke-width="1.5"/></svg>office@brookvalepoultry.com</div>
    </div>

    <h1 class="fax-title">FAX</h1>

    <div class="fax-fields">
      <div class="fax-fields__row"><div class="fax-field fax-field--wide">To :</div><div class="fax-field fax-field--narrow">From :</div></div>
      <div class="fax-fields__row"><div class="fax-field fax-field--wide">Fax :</div><div class="fax-field fax-field--narrow">Pages :</div></div>
      <div class="fax-fields__row"><div class="fax-field fax-field--wide">Phone :</div><div class="fax-field fax-field--narrow">Date :</div></div>
      <div class="fax-fields__row"><div class="fax-field fax-field--wide">Re :</div><div class="fax-field fax-field--narrow">CC :</div></div>
    </div>

    <div class="fax-options">
      <div class="fax-option" style="left:0"><span class="fax-option__box"></span>Urgent</div>
      <div class="fax-option" style="left:74px"><span class="fax-option__box"></span>For Review</div>
      <div class="fax-option" style="left:169px"><span class="fax-option__box"></span>Please Comment</div>
      <div class="fax-option" style="left:290px"><span class="fax-option__box"></span>Please Reply</div>
      <div class="fax-option" style="left:395px"><span class="fax-option__box"></span>Please Recycle</div>
    </div>

    <footer class="footer">
      <div class="footer__stripe footer__stripe--red"></div>
      <div class="footer__stripe footer__stripe--yellow"></div>
      <div class="footer__band">
        <div class="footer__street">Settlers Corner Road KERRIDGE SA 5258</div>
      </div>
    </footer>
  </section>

</body>
</html>
```